Professional Flyer - for Brindle Vale

Create a professional looking flyer than the one attached.
Change headline to: Hemp Homes the next Evolution in Green Building
Sub headline: Sustainable, Durable and Healthier to Live in
Delete the address below the headline.
Use as much as the other information that makes sense and that you have room for.

Thanks!

```html
<!DOCTYPE html>
<html lang="en">
<head>
<meta charset="utf-8">
<title>Hemp Homes Flyer</title>
<link href="https://fonts.googleapis.com/css2?family=Arimo:ital,wght@0,700;1,400&family=Cantarell&family=Montserrat:wght@500;700&display=swap" rel="stylesheet">
<style>
  :root {
    --backdrop: #0d0f1e;
    --teal: #2bb5d9;
    --ink: #1d1d1d;
    --dot: #27a6d6;
    --contact-teal: #22aed6;
    --contact-rust: #b0531e;
    --white: #ffffff;
  }
  html, body {
    margin: 0;
    width: 1200px;
    height: 1171px;
    overflow: hidden;
    background: var(--backdrop);
  }
  .flyer {
    position: absolute;
    left: 107px;
    top: 236px;
    width: 988px;
    height: 699px;
    background: var(--white);
    overflow: hidden;
  }
  .flyer__waves {
    position: absolute;
    inset: 0;
    width: 100%;
    height: 100%;
  }
  .headline {
    position: absolute;
    top: 10px;
    left: 0;
    width: 100%;
    margin: 0;
    text-align: center;
    font-family: "Arimo", Arial, sans-serif;
    font-weight: 700;
    font-size: 44px;
    line-height: 46px;
    color: var(--white);
  }
  .headline span { display: block; }
  .subheadline {
    position: absolute;
    top: 111px;
    left: 0;
    width: 100%;
    margin: 0;
    text-align: center;
    font-family: "Cantarell", "Trebuchet MS", sans-serif;
    font-size: 25px;
    color: var(--ink);
  }
  .features {
    position: absolute;
    top: 222px;
    left: 52px;
    display: flex;
    gap: 22px;
    font-family: "Montserrat", Arial, sans-serif;
    font-weight: 500;
    font-size: 13.5px;
    line-height: 17px;
    color: var(--ink);
  }
  .features ul { list-style: none; margin: 0; padding: 0; }
  .features li { position: relative; padding-left: 17px; white-space: nowrap; }
  .features li::before {
    content: "";
    position: absolute;
    left: 0;
    top: 4px;
    width: 9px;
    height: 9px;
    border-radius: 50%;
    background: var(--dot);
  }
  .features ul.features__col--3 { margin-top: -12px; }
  .listing {
    position: absolute;
    top: 330px;
    left: 76px;
    width: 556px;
    margin: 0;
    font-family: "Arimo", Arial, sans-serif;
    font-style: italic;
    font-size: 17px;
    line-height: 26px;
    text-align: justify;
    color: var(--ink);
  }
  .listing p { margin: 0; }
  .listing .price { padding-left: 20px; text-align: left; }
  .home-photo {
    position: absolute;
    left: 716px;
    top: 157px;
    width: 264px;
    height: 262px;
    border: 4px solid var(--teal);
    border-radius: 22px;
    background: linear-gradient(160deg, #eef3ea 0%, #9bb07a 45%, #7a5a36 70%, #b9b9a8 100%);
  }
  .contact {
    position: absolute;
    left: 772px;
    top: 448px;
    font-family: "Montserrat", Arial, sans-serif;
    font-weight: 700;
    font-size: 17px;
    line-height: 21px;
  }
  .contact__company { color: var(--contact-teal); margin: 0; }
  .contact__question { color: var(--contact-rust); margin: 18px 0 0; }
</style>
</head>
<body>
  <main class="flyer">
    <svg class="flyer__waves" viewBox="0 0 988 699" preserveAspectRatio="none" aria-hidden="true">
      <defs>
        <linearGradient id="brandGradient" x1="0" y1="0" x2="1" y2="0">
          <stop offset="0" stop-color="#2bb5d9"/>
          <stop offset="0.45" stop-color="#48c4bd"/>
          <stop offset="1" stop-color="#c3d92e"/>
        </linearGradient>
        <linearGradient id="limeGradient" x1="0" y1="0" x2="1" y2="0">
          <stop offset="0" stop-color="#c3d92e"/>
          <stop offset="1" stop-color="#6cc66a"/>
        </linearGradient>
      </defs>
      <path d="M0 0H988V120C900 95 820 120 720 150C560 180 380 170 240 160C140 155 60 170 0 200Z" fill="url(#brandGradient)"/>
      <path d="M0 200C90 165 200 150 330 168C470 185 560 200 700 178C560 205 430 212 300 200C180 190 90 200 0 232Z" fill="url(#limeGradient)" opacity="0.85"/>
      <path d="M240 160C360 150 440 168 500 175C430 176 360 172 240 160Z" fill="#2bb5d9" opacity="0.7"/>
      <path d="M460 195C580 205 700 196 820 175C740 205 620 215 460 195Z" fill="#c3d92e"/>
      <path d="M0 525C120 545 220 600 360 612C200 610 90 590 0 580Z" fill="url(#limeGradient)"/>
      <path d="M0 590C150 615 300 640 480 625C650 612 820 598 988 604V699H0Z" fill="url(#brandGradient)"/>
      <path d="M0 640C180 660 360 660 520 640C680 622 840 615 988 628V648C820 638 660 650 520 665C360 682 160 680 0 665Z" fill="#ffffff"/>
    </svg>

    <h1 class="headline">
      <span>HEMP HOMES THE NEXT EVOLUTION</span>
      <span>IN GREEN BUILDING</span>
    </h1>
    <p class="subheadline">Sustainable, Durable and Healthier to Live in</p>

    <div class="features">
      <ul class="features__col">
        <li>Hight Thermal Insulation</li>
        <li>Hight Sound Insulation</li>
        <li>Hight Thermal Inertia</li>
        <li>Good Vapor Permeability</li>
      </ul>
      <ul class="features__col">
        <li>Good Flexibility</li>
        <li>Fire Resistant</li>
        <li>Pest Resistant</li>
        <li>Can reduce CO-2 Emissions</li>
      </ul>
      <ul class="features__col features__col--3">
        <li>Cut Energy Bills by 50-70%</li>
        <li>Up to R-50 wall Insulation</li>
        <li>Mold Resistant!</li>
      </ul>
    </div>

    <div class="listing">
      <p>Seller is offering this build job as a 1200 sq. ft 3 Br.-2Ba W/400 sq ft garage on 3 acres on blacktop near Brindle Vale!</p>
      <p>HEMPCRETE construction is newer to our area but used Commonly Worldwide as an Economically &amp; Enviromentally sound choice of building materials! this plan will offer a solar unit as well to reduce energy costs! AND HOME WILL HAVE GEO THERMAL &amp; LED PACKAGE!! REDUCE YOUR MONTHLY UTILITY BULLS TO BUDGET FRIENDLY $$'s !! AND . . . . UP TO $15,00 TAX CREDIT!</p>
      <p class="price">Upgraded w/GEO Thermal &amp; LED $219,900K</p>
    </div>

    <div class="home-photo" role="img" aria-label="Illustration of a two-storey timber hemp home with solar panels on the roof, trees and a stone path"></div>

    <div class="contact">
      <p class="contact__company">ASH BRO'S<br>CONSTRUCTION<br>555-014-2279</p>
      <p class="contact__question">QUESTION ?? Or<br>Need more info ??<br>call Dale Today!!</p>
    </div>
  </main>
</body>
</html>
```